Brochure Design Project

We require a brochure that will look good as a PDF emailed to clients, and will also look good as a centre spread 2 page double sided glossy A3 (folded into A4) brochure for hand deliveries. Only 3 sides need to be designed. Imagine an A3 paper folded in half, like a book. The front cover should have logos, company name and maybe a short blurb. When you open the "book", the centerfold should show all the text and photos. The back can be blank, or minimal design.
All text has been provided. The 2 logos are essential (ie the company logo and the master builder's logo. Add as many photos as you can fit. The photos are labelled 1 to 9. Photos 1, 6, 8 and 9 are essential. The rest are highly preferred but see how many you can fit.
I have high res photos and logos etc. If you are the winning designer, I will obviously send all hi-res files to you for the final copy.
Good luck.
Project Deadline Extended
Some things to note:
Target Market(s)
Architects, property developers, bankers, construction professionals, government clients.
Industry/Entity Type
It Company
Look and feel
Each slider illustrates characteristics of the customer's brand and the style your logo design should communicate.

```html
<!DOCTYPE html>
<html lang="en">
<head>
<meta charset="utf-8">
<title>Valorian Homes – Brochure Cover Spread</title>
<link rel="stylesheet" href="https://fonts.googleapis.com/css2?family=Cinzel:wght@500&family=Cormorant+Garamond:ital,wght@1,400&family=PT+Sans:wght@400&display=swap">
<style>
  :root {
    --paper: #efdeb0;
    --brand-gold: #a9802c;
    --homes-grey: #78787e;
    --contact-ink: #6f7186;
    --white: #ffffff;
    --spine: #f7ecd0;
  }
  * { margin: 0; padding: 0; box-sizing: border-box; }
  html, body { width: 1200px; height: 848px; overflow: hidden; background: var(--white); }
  .spread { position: relative; width: 1200px; height: 848px; display: flex; }

  .back-cover { width: 596px; height: 848px; background: var(--paper); position: relative; }
  .spine { width: 2px; height: 848px; background: var(--spine); }

  .contact-block {
    position: absolute; left: 0; width: 596px; top: 640px;
    text-align: center; color: var(--contact-ink);
    font-family: "PT Sans", sans-serif; font-size: 8.6px; line-height: 11px;
  }
  .contact-block p { margin-bottom: 11px; }
  .contact-role { font-size: 5.5px; line-height: 7px; display: block; }
  .contact-lines { display: inline-block; text-align: left; }
  .contact-lines .label { display: inline-block; width: 30px; }

  .front-cover { position: relative; width: 602px; height: 848px; overflow: hidden; }
  .front-cover svg.backdrop { position: absolute; inset: 0; }

  .brand-mark {
    position: absolute; left: 84px; top: 268px; width: 76px; height: 76px;
    border-radius: 50%; background: var(--brand-gold);
  }
  .brand-name {
    position: absolute; left: 164px; top: 284px;
    font-family: "Cinzel", serif; font-weight: 500; color: var(--brand-gold);
    font-size: 62px; line-height: 70px; letter-spacing: 0;
  }
  .brand-sub {
    position: absolute; left: 0; width: 602px; top: 370px; text-align: center;
    padding-left: 8px;
    font-family: "Cinzel", serif; font-weight: 500; color: var(--homes-grey);
    font-size: 44px; line-height: 50px; letter-spacing: 2px;
  }
  .tagline {
    position: absolute; left: 0; width: 602px; top: 426px; text-align: center;
    font-family: "Cormorant Garamond", serif; font-style: italic; font-size: 19.5px;
    color: var(--white);
  }
</style>
</head>
<body>
<main class="spread">
  <section class="back-cover" aria-label="Back cover">
    <div class="contact-block">
      <p>Contact Us</p>
      <p>Marcus Ellery<span class="contact-role">Chief Executive Officer</span></p>
      <p>Valorian Group<br>Suite 204, 52 Elm Rd<br>Ashby, VIC, 3188</p>
      <p><span class="contact-lines"><span class="label">Phone</span>: 0400 000 123<br><span class="label">Fax</span>: 03 9000 4567</span></p>
      <p>marcus.ellery@valorianfinance.com.au<br>www.valorianhomes.com.au</p>
    </div>
  </section>

  <div class="spine"></div>

  <section class="front-cover" aria-label="Front cover">
    <svg class="backdrop" width="602" height="848" viewBox="0 0 602 848">
      <defs>
        <linearGradient id="upperTone" x1="0" y1="0" x2="0" y2="1">
          <stop offset="0" stop-color="#e6cf9c"/>
          <stop offset="1" stop-color="#f2e2b8"/>
        </linearGradient>
        <radialGradient id="logoGlow" cx="320" cy="320" r="260" gradientUnits="userSpaceOnUse">
          <stop offset="0" stop-color="#fffaf0" stop-opacity="1"/>
          <stop offset="0.45" stop-color="#f8ecd0" stop-opacity="0.8"/>
          <stop offset="1" stop-color="#f2e2b8" stop-opacity="0"/>
        </radialGradient>
        <linearGradient id="lowerBand" x1="0" y1="0" x2="0" y2="1">
          <stop offset="0" stop-color="#a77a33"/>
          <stop offset="0.35" stop-color="#c59f5f"/>
          <stop offset="0.75" stop-color="#dfc48c"/>
          <stop offset="1" stop-color="#e8d3a2"/>
        </linearGradient>
        <linearGradient id="seam" x1="0" y1="0" x2="1" y2="0">
          <stop offset="0" stop-color="#ffffff" stop-opacity="0"/>
          <stop offset="0.5" stop-color="#ffffff" stop-opacity="0.22"/>
          <stop offset="1" stop-color="#ffffff" stop-opacity="0"/>
        </linearGradient>
        <radialGradient id="linework" cx="300" cy="620" r="320" gradientUnits="userSpaceOnUse">
          <stop offset="0" stop-color="#f6e7c2" stop-opacity="0.35"/>
          <stop offset="1" stop-color="#f6e7c2" stop-opacity="0"/>
        </radialGradient>
      </defs>

      <rect x="0" y="0" width="602" height="420" fill="url(#upperTone)"/>
      <polygon points="0,0 298,0 298,420 0,420" fill="#c9a462" opacity="0.18"/>
      <polygon points="0,0 298,420 0,420" fill="#ffffff" opacity="0.12"/>
      <polygon points="602,40 420,420 602,420" fill="#ffffff" opacity="0.14"/>
      <rect x="0" y="0" width="602" height="420" fill="url(#logoGlow)"/>

      <rect x="0" y="420" width="602" height="428" fill="url(#lowerBand)"/>
      <polygon points="0,420 298,420 298,848 0,848" fill="#ffffff" opacity="0.06"/>
      <polygon points="602,540 430,848 602,848" fill="#ffffff" opacity="0.12"/>
      <rect x="268" y="0" width="60" height="848" fill="url(#seam)"/>
      <rect role="img" aria-label="Fine flowing gold line-work pattern" x="0" y="420" width="602" height="428" fill="url(#linework)"/>
    </svg>

    <div class="brand-mark" aria-hidden="true"></div>
    <span class="brand-name">VALORIAN</span>
    <span class="brand-sub">HOMES</span>
    <p class="tagline">Your professional Property Development and Construction Partner</p>
  </section>
</main>
</body>
</html>
```